Modernise Business Card

Our company has been operating for 10 years. With the start of the new decade we are looking to refresh our business card design. We manufacture a range of industrial product shipping to customers internationally. A copy of our current card, both sides, is attached. We are looking for a mature professional appearance.

```html
<!DOCTYPE html>
<html lang="en">
<head>
<meta charset="utf-8">
<title>Corvane Business Card</title>
<link href="https://fonts.googleapis.com/css2?family=Lato:wght@400;700;900&display=swap" rel="stylesheet">
<style>
  :root {
    --brand-blue: #1fa3dc;
    --brand-blue-pale: #e6f4fb;
    --ink: #2b2b2b;
    --paper: #ffffff;
    --accent-brown: #5a4a42;
    --backdrop: #2a2a2a;
  }
  * { box-sizing: border-box; margin: 0; padding: 0; }
  html, body { width: 1200px; height: 878px; overflow: hidden; }
  body {
    background: var(--backdrop);
    font-family: "Lato", sans-serif;
    display: flex;
    align-items: center;
    justify-content: center;
    gap: 48px;
  }
  .card {
    position: relative;
    width: 540px;
    height: 310px;
    overflow: hidden;
    box-shadow: 0 10px 28px rgba(0,0,0,.5);
  }
  /* Front */
  .card-front {
    background: var(--brand-blue);
    display: flex;
    flex-direction: column;
    align-items: center;
    justify-content: center;
    gap: 14px;
  }
  .wordmark {
    font-weight: 900;
    font-size: 86px;
    letter-spacing: -1px;
    color: var(--paper);
    line-height: 1;
  }
  .tagline {
    font-size: 13px;
    letter-spacing: 1.4px;
    color: var(--paper);
  }
  /* Back */
  .card-back { background: var(--paper); }
  .back-panel {
    position: absolute;
    right: 0; top: 22px;
    width: 250px; height: 252px;
    background: var(--brand-blue-pale);
  }
  .holder {
    position: absolute; left: 30px; top: 26px;
  }
  .holder-name {
    font-weight: 900; font-size: 27px; color: var(--brand-blue); line-height: 1;
  }
  .holder-role {
    font-size: 13px; color: var(--ink); margin-top: 3px;
  }
  .back-wordmark {
    position: absolute; right: 34px; top: 108px;
    font-weight: 900; font-size: 58px; color: var(--brand-blue); line-height: 1;
  }
  .contact-list {
    position: absolute; left: 30px; top: 142px;
    list-style: none;
    font-size: 15px; color: var(--ink);
  }
  .contact-list li {
    display: flex; align-items: center; gap: 12px; height: 24px;
  }
  .contact-list svg { width: 14px; height: 14px; fill: var(--brand-blue); flex: none; }
  .address {
    position: absolute; left: 18px; top: 246px; right: 30px;
    display: flex; gap: 10px;
    font-size: 15px; color: var(--ink); line-height: 1.2;
    border-top: 1px solid #bfe3f3; padding-top: 6px;
  }
  .address svg { width: 14px; height: 16px; fill: var(--brand-blue); flex: none; margin-top: 2px; }
  .base-band {
    position: absolute; left: 0; right: 0; bottom: 0; height: 8px;
    background: var(--brand-blue);
  }
  .base-band::before {
    content: ""; position: absolute; left: 0; top: 0; width: 40px; height: 8px;
    background: var(--accent-brown);
  }
</style>
</head>
<body>
  <section class="card card-front">
    <div class="wordmark">Corvane</div>
    <p class="tagline">HYDRAULIC ADAPTERS HOSE FITTINGS QUICK COUPLINGS</p>
  </section>

  <section class="card card-back">
    <div class="back-panel"></div>
    <div class="holder">
      <h1 class="holder-name">Alan Brennick</h1>
      <p class="holder-role">Founder &amp; CEO</p>
    </div>
    <div class="back-wordmark">Corvane</div>
    <ul class="contact-list">
      <li><svg viewBox="0 0 24 24"><path d="M6.6 10.8a15 15 0 0 0 6.6 6.6l2.2-2.2c.3-.3.7-.4 1-.2 1.1.4 2.3.6 3.6.6.6 0 1 .4 1 1V20c0 .6-.4 1-1 1A17 17 0 0 1 3 4c0-.6.4-1 1-1h3.5c.6 0 1 .4 1 1 0 1.3.2 2.5.6 3.6.1.3 0 .7-.2 1z"/></svg>+86 139 5520 0417 (China)</li>
      <li><svg viewBox="0 0 24 24"><path d="M6.6 10.8a15 15 0 0 0 6.6 6.6l2.2-2.2c.3-.3.7-.4 1-.2 1.1.4 2.3.6 3.6.6.6 0 1 .4 1 1V20c0 .6-.4 1-1 1A17 17 0 0 1 3 4c0-.6.4-1 1-1h3.5c.6 0 1 .4 1 1 0 1.3.2 2.5.6 3.6.1.3 0 .7-.2 1z"/></svg>+61 412 775 803 (Australia)</li>
      <li><svg viewBox="0 0 24 24"><path d="M2 5h20v14H2zm2 2v.5l8 5 8-5V7l-8 5z"/></svg>abrennick@corvanefittings.com</li>
      <li><svg viewBox="0 0 24 24"><circle cx="12" cy="12" r="10"/></svg>www.corvanefittings.com</li>
    </ul>
    <div class="address">
      <svg viewBox="0 0 24 28"><path d="M12 0a10 10 0 0 0-10 10c0 7.5 10 18 10 18s10-10.5 10-18A10 10 0 0 0 12 0zm0 14a4 4 0 1 1 0-8 4 4 0 0 1 0 8z"/></svg>
      <p>1208-5, Lian Tai Building 417 Qiming Road,<br>Jiangbei District Ningbo 315020 China</p>
    </div>
    <div class="base-band"></div>
  </section>
</body>
</html>
```